Bay & Meadow Property Services Tri-fold sales & marketing brochure

We need a tri-fold brochure that describes our three lines of business and the various services within each line to use in sales and marketing efforts.
See website for additional background info:
https://halvernq7.example-host.com/

Target Market(s)

Real Estate Investors & owners in Residential Rental, Short-term Rentals, and Mini/Maxi Storage Rental markets

Requirements
Must have
• See attached logo, use color scheme & font styles to match. Make sure to utilize photos to enhance look/feel.

```html
<!DOCTYPE html>
<html lang="en">
<head>
<meta charset="utf-8">
<title>Bay &amp; Meadow Property Services – Tri-fold Brochure</title>
<link href="https://fonts.googleapis.com/css2?family=Montserrat:ital,wght@0,400;0,600;0,700;1,500;1,700&family=Quicksand:wght@400;500&display=swap" rel="stylesheet">
<style>
  :root {
    --ink: #0f0f10;
    --paper: #ffffff;
    --mist: #e4e4e6;
    --slate: #7a7a7c;
    --accent: #1b8ec2;
    --body-text: #2a2a2a;
    --soft-text: #6d6d6d;
  }
  * { margin: 0; padding: 0; box-sizing: border-box; }
  html, body { width: 1200px; height: 801px; overflow: hidden; background: #d9d6d3; }
  .brochure { position: relative; width: 1200px; height: 801px; font-family: "Quicksand", sans-serif; color: var(--body-text); }
  .brochure-shapes { position: absolute; inset: 0; }
  .block { position: absolute; }

  .brand { display: flex; align-items: center; gap: 8px; font-family: "Montserrat", sans-serif; font-weight: 600; font-size: 11px; letter-spacing: 1.5px; text-transform: uppercase; line-height: 1.25; }
  .brand-dot { width: 22px; height: 22px; border-radius: 50%; background: var(--accent); flex: none; }
  .brand--on-dark { color: var(--paper); }
  .brand--on-light { color: var(--ink); }

  .offer-title { font-family: "Montserrat", sans-serif; font-weight: 700; font-style: italic; font-size: 15px; line-height: 1.3; color: var(--ink); margin-bottom: 8px; }
  .offer-copy { font-size: 10px; line-height: 1.55; margin-bottom: 16px; }
  .list-title { font-family: "Montserrat", sans-serif; font-weight: 700; font-style: italic; font-size: 11px; color: var(--ink); margin-bottom: 5px; }
  .service-list { list-style: none; font-size: 10px; line-height: 1.55; font-style: italic; }
  .offer--muted .offer-title, .offer--muted .list-title { color: #4a4a4a; }
  .offer--muted .offer-copy, .offer--muted .service-list { color: var(--soft-text); }

  .contact-list { list-style: none; font-size: 10px; color: var(--paper); }
  .contact-list li { display: flex; align-items: center; gap: 9px; margin-bottom: 8px; }
  .contact-icon { width: 16px; height: 16px; flex: none; }

  .cover-title { font-family: "Montserrat", sans-serif; font-weight: 700; font-size: 23px; color: var(--paper); letter-spacing: 1px; line-height: 1.2; }
  .cover-sub { font-family: "Montserrat", sans-serif; font-weight: 400; font-size: 12px; color: var(--paper); letter-spacing: 4px; margin-top: 3px; }
  .cover-rule { width: 110px; height: 3px; background: var(--accent); margin: 10px 0 14px; }
  .cover-lead { font-family: "Montserrat", sans-serif; font-weight: 700; font-size: 11px; color: var(--paper); margin-bottom: 5px; }
  .cover-copy { font-size: 10.5px; line-height: 1.5; color: var(--paper); margin-bottom: 16px; }
  .expertise-title { font-family: "Montserrat", sans-serif; font-weight: 700; font-size: 10px; color: var(--paper); margin-bottom: 5px; }
  .expertise-list { list-style: none; font-size: 9px; line-height: 1.5; color: var(--paper); }
</style>
</head>
<body>
<main class="brochure">
  <svg class="brochure-shapes" width="1200" height="801" viewBox="0 0 1200 801" aria-hidden="true">
    <defs>
      <linearGradient id="mistFade" x1="0" y1="0" x2="1" y2="1">
        <stop offset="0" stop-color="#ffffff"/><stop offset="1" stop-color="#c9c9cb"/>
      </linearGradient>
      <linearGradient id="slateBand" x1="0" y1="0" x2="1" y2="0">
        <stop offset="0" stop-color="#5e5e60"/><stop offset="1" stop-color="#9b9b9d"/>
      </linearGradient>
    </defs>
    <rect x="0" y="0" width="800" height="801" fill="var(--paper)"/>
    <polygon class="panel-one-head" points="0,0 400,0 400,157 0,180" fill="var(--ink)"/>
    <polygon class="panel-two-head" points="400,0 800,0 800,60 400,157" fill="url(#mistFade)"/>
    <polygon class="panel-one-foot" points="0,610 400,690 400,801 0,801" fill="var(--ink)"/>
    <polygon class="panel-two-foot" points="400,690 800,655 800,801 400,801" fill="url(#slateBand)"/>
    <rect x="800" y="0" width="400" height="801" fill="var(--mist)"/>
    <polygon class="cover-dark" points="800,230 960,130 1200,560 1200,801 800,801" fill="var(--ink)"/>
    <line x1="968" y1="126" x2="1200" y2="542" stroke="var(--accent)" stroke-width="7"/>
    <line x1="400" y1="0" x2="400" y2="801" stroke="#000" stroke-opacity=".08"/>
    <line x1="800" y1="0" x2="800" y2="801" stroke="#000" stroke-opacity=".08"/>
  </svg>

  <svg class="block" style="left:0;top:0" width="800" height="400" viewBox="0 0 800 400" role="img" aria-label="Photo of a large brick family home with a green lawn and trees at sunset">
    <defs>
      <linearGradient id="homePhoto" x1="0" y1="0" x2="1" y2="0.4">
        <stop offset="0" stop-color="#3f5a24"/><stop offset=".35" stop-color="#7a3f2c"/>
        <stop offset=".7" stop-color="#a8806a"/><stop offset="1" stop-color="#d8dcc4"/>
      </linearGradient>
    </defs>
    <polygon points="0,180 520,150 800,60 800,330 400,330 0,290" fill="url(#homePhoto)"/>
  </svg>

  <div class="block brand brand--on-dark" style="left:200px;top:40px"><span class="brand-dot"></span><span>Bay &amp; Meadow<br>Property Services</span></div>

  <section class="block offer" style="left:26px;top:340px;width:355px">
    <h2 class="offer-title">Locate High-Value Residential Investment Opportunities</h2>
    <p class="offer-copy">At Bay &amp; Meadow Property Services, we specialize in helping investors uncover profitable and strategic residential real estate opportunities before they hit the mainstream market. Whether you're building a new portfolio or expanding an existing one, our data-driven insights, local expertise, and industry connections empower you to make confident, forward-thinking investment decisions. We don't just find properties—we find potential.</p>
    <h3 class="list-title">Our Services Include:</h3>
    <ul class="service-list">
      <li>*Market Research &amp; Feasibility Analysis</li>
      <li>*Off-Market Property Sourcing</li>
      <li>*Investment Matching</li>
      <li>*Due Diligence Support</li>
      <li>*Redevelopment Potential Identification</li>
    </ul>
  </section>

  <ul class="block contact-list" style="left:34px;top:692px">
    <li><svg class="contact-icon" viewBox="0 0 16 16"><circle cx="8" cy="8" r="8" fill="#fff"/><rect x="4" y="5" width="8" height="6" fill="none" stroke="#111" stroke-width="1"/><path d="M4 5l4 3.5L12 5" fill="none" stroke="#111" stroke-width="1"/></svg>info@bayandmeadowproperty.com</li>
    <li><svg class="contact-icon" viewBox="0 0 16 16"><circle cx="8" cy="8" r="8" fill="#fff"/><circle cx="8" cy="8" r="4" fill="none" stroke="#111"/><path d="M4 8h8M8 4v8" stroke="#111"/></svg>halvernq7.example-host.com</li>
    <li><svg class="contact-icon" viewBox="0 0 16 16"><circle cx="8" cy="8" r="8" fill="#fff"/><rect x="5.5" y="3.5" width="5" height="9" rx="1" fill="#111"/></svg>(555) 0142-386</li>
    <li><svg class="contact-icon" viewBox="0 0 16 16"><circle cx="8" cy="8" r="8" fill="#fff"/><path d="M8 13s-3.5-3.6-3.5-6a3.5 3.5 0 0 1 7 0c0 2.4-3.5 6-3.5 6z" fill="#111"/></svg>412 Alderbrook Lane Fairhaven, WI 50000</li>
  </ul>

  <section class="block offer offer--muted" style="left:426px;top:380px;width:350px">
    <h2 class="offer-title">Locate High-Value Residential Investment Opportunities</h2>
    <p class="offer-copy">At Bay &amp; Meadow Property Services, we specialize in helping investors uncover profitable and strategic residential real estate opportunities before they hit the mainstream market. Whether you're building a new portfolio or expanding an existing one, our data-driven insights, local expertise, and industry connections empower you to make confident, forward-thinking investment decisions. We don't just find properties—we find potential.</p>
    <h3 class="list-title">Our Services Include:</h3>
    <ul class="service-list">
      <li>*Market Research &amp; Feasibility Analysis</li>
      <li>*Off-Market Property Sourcing</li>
      <li>*Investment Matching</li>
      <li>*Due Diligence Support</li>
      <li>*Redevelopment Potential Identification</li>
    </ul>
  </section>

  <ul class="block contact-list" style="left:440px;top:703px">
    <li><svg class="contact-icon" viewBox="0 0 16 16"><circle cx="8" cy="8" r="8" fill="#fff"/><rect x="4" y="5" width="8" height="6" fill="none" stroke="#555" stroke-width="1"/><path d="M4 5l4 3.5L12 5" fill="none" stroke="#555" stroke-width="1"/></svg>info@bayandmeadowproperty.com</li>
    <li><svg class="contact-icon" viewBox="0 0 16 16"><circle cx="8" cy="8" r="8" fill="#fff"/><circle cx="8" cy="8" r="4" fill="none" stroke="#555"/><path d="M4 8h8M8 4v8" stroke="#555"/></svg>halvernq7.example-host.com</li>
    <li><svg class="contact-icon" viewBox="0 0 16 16"><circle cx="8" cy="8" r="8" fill="#fff"/><rect x="5.5" y="3.5" width="5" height="9" rx="1" fill="#555"/></svg>(555) 0142-386</li>
    <li><svg class="contact-icon" viewBox="0 0 16 16"><circle cx="8" cy="8" r="8" fill="#fff"/><path d="M8 13s-3.5-3.6-3.5-6a3.5 3.5 0 0 1 7 0c0 2.4-3.5 6-3.5 6z" fill="#555"/></svg>412 Alderbrook Lane Fairhaven, WI 50000</li>
  </ul>

  <div class="block brand brand--on-light" style="left:1020px;top:56px"><span class="brand-dot"></span><span>Bay &amp; Meadow<br>Property Services</span></div>

  <section class="block cover" style="left:826px;top:318px;width:255px">
    <h1 class="cover-title">BAY &amp; MEADOW</h1>
    <p class="cover-sub">PROPERTY SERVICES</p>
    <div class="cover-rule"></div>
    <p class="cover-lead">Where Expertise Meets Exceptional Returns</p>
    <p class="cover-copy">At Bay &amp; Meadow Property Services, we are your trusted partner in unlocking the full potential of your real estate investments. With unparalleled expertise across three key sectors—long-term residential rentals, short-term vacation rentals (like StayNest and HomeHopper), and mini-maxi storage—our white-glove services are designed to elevate your property's value and maximize your financial returns.</p>
    <h3 class="expertise-title">Our Expertise Includes:</h3>
    <ul class="expertise-list">
      <li>1- Investment &amp; Opportunity Evaluation: Finding and analyzing lucrative real estate projects tailored to your goals.</li>
      <li>2- Design &amp; Development Management: Overseeing new construction or refurbishment projects to enhance property value.</li>
      <li>3- Compliance &amp; Permitting: Navigating local regulations and approvals with ease.</li>
      <li>4- Tenant &amp; Property Management: Providing seamless day-to-day management for tenants and properties to ensure optimal satisfaction and financial performance.</li>
      <li>5- Strategic Exits: Guiding you through the sale process to secure top dollar for your investments.</li>
    </ul>
  </section>
</main>
</body>
</html>
```